Bright Ridge Ore is a new gold exploration company. Their mandate is discovering new gold deposits.
Bright Ridge Ore will need to make public presentations and send out news releases on company letterheads.

We have recently designed a logo.

What we need:
We need a Powerpoint Template and Word template for corporate communications.

We need you to:

0) Provide a Corporate Colour Palette / Colour Swatch that we can load into powerpoint as our colour palette.

1) Using that colour palette, design a POWERPOINT presentation TEMPLATE that works with our logo – and works with but doesn't necessarily require Trajan Pro font. We’ll need a slide background, image and text layout, text-image balance, recommended font size, colours, composition

2) We’ll want to see your Powerpoint templates – we need Front page, Content Page, Divider Page, Back page with a good background, header, footer, and layout
--> Deliverable is a Powerpoint Template design file including colour palette that will automatically assign colours to charts / graphs, background, text etc

3) We’ll want to see your WORD REPORT templates – we need a Front page, Content Page, Divider Page, Back page with a good background, header, footer, title, section heading and sub-section font styles and layout for lengthy company reports. Note our logo is in Trajan Pro.

4) AND we need a LETTERHEAD (Word template) with front page header, footer, memo layout and subsequent pages with header and footer.

and 5) An EMAIL SIGNATURE
Please supply results as POWERPOINT and WORD

We want to see inverted colour ideas as well (our logo shows blacktext, we'd like to see ideas with White text (or another colour that works)

For colour ideas and a contribution to our Divider page we have loaded up photographs in a .pptx file below. These are the sorts of hues many of our future photos will generate.. please keep it in mind.

Our upload also shows some constraints - logo bottom left - only use 2.72cm in your banner.. etc.. it's all there

Do a great job and there may be more to come - we also need to build a new website

It's a challenge, but we've seen what pixel guild can do and we know you can make something great with what we have.

Do what you can.. we may award even if not all items are complete.
Start with Colour Palette, Email signature and Letterhead.
Then Powerpoint.
Word can be last.

Looking forward to it...

Target Market(s)

Investors that expect to see corporate presentations with a style and professional look that you see from companies like Tovarine Holdings, KPL, gold exploration, Halvecor, Quembrata, Ostrivale, Pelusko Gold, Vantrel, Gold Nexa, etc...

Industry/Entity Type

Mining

Font styles to use
Serif
Sans Serif

Requirements
Must have
• A colour palette that can be applied in PowerPoint Design tab
• A PowerPoint Template .POTX file
• - Title page
• - Content page
• - Divider page
• - Backpage
• no more than 2.75cm banner, no more than 1.5cm footer
• follow instructions as shown in .pdf upload (content slide title position, logo position - others are flexible
• Must use logo uploaded
• Email signature (.eps, .ai, .png files)
• Word letterhead (.docx and .DOTX)
• *Update - 1st Feb - Business cards are to be Embossed with Sunken lettering
Nice to have
• Layout recommendations - example showing text / image balance
Should not have
• australia flag, southern cross, kangaroos...

```html
<!DOCTYPE html>
<html lang="en">
<head>
<meta charset="utf-8">
<title>Bright Ridge Ore – Presentation Template</title>
<link rel="stylesheet" href="https://fonts.googleapis.com/css2?family=Cinzel:wght@400;600&family=Open+Sans:wght@400;600&display=swap">
<style>
  :root {
    --gold: #a8862c;
    --gold-band: #ad8d34;
    --gold-light: #e3cc94;
    --ink: #2a2a2a;
    --charcoal: #3c3c3c;
    --grey-text: #666;
    --rule-dark: #444;
    --paper: #ffffff;
    --canvas: #ffffff;
    --panel-line: #e6e6e6;
  }
  * { margin: 0; padding: 0; box-sizing: border-box; }
  html, body { width: 1200px; height: 1159px; overflow: hidden; background: var(--canvas); }
  body { position: relative; font-family: "Open Sans", Arial, sans-serif; color: var(--ink); }

  .slide {
    position: absolute; width: 551px; height: 310px; background: var(--paper);
    box-shadow: 0 1px 4px rgba(0,0,0,.25); overflow: hidden;
  }
  .slide--cover { left: 29px; top: 29px; }
  .slide--content { left: 620px; top: 29px; }
  .slide--divider-a { left: 29px; top: 404px; }
  .slide--divider-b { left: 620px; top: 404px; }
  .slide--back { left: 322px; top: 786px; }

  .slide-label {
    position: absolute; width: 551px; text-align: center;
    font-size: 19px; letter-spacing: .5px; color: var(--ink);
  }

  .rule { position: absolute; left: 0; width: 100%; height: 2px; background: var(--gold); }

  .brand { position: absolute; display: flex; align-items: center; gap: 8px; }
  .brand__dot { width: 22px; height: 22px; border-radius: 50%; background: var(--gold); flex: none; }
  .brand__name { font-family: "Cinzel", Georgia, serif; font-weight: 400; color: var(--charcoal); font-size: 17px; letter-spacing: .5px; }

  .cover-title {
    position: absolute; left: 17px; top: 176px;
    font-family: "Cinzel", Georgia, serif; font-size: 26px; color: var(--gold); letter-spacing: 1px;
  }
  .cover-text { position: absolute; left: 17px; top: 207px; width: 300px; font-size: 5.5px; line-height: 9px; color: var(--grey-text); }

  .page-head { position: absolute; left: 17px; top: 15px; }
  .page-head__title { font-family: "Cinzel", Georgia, serif; font-size: 12px; letter-spacing: .5px; color: var(--ink); }
  .page-head__title span { color: var(--gold); }
  .page-head__sub { font-size: 7px; color: var(--ink); margin-top: 1px; }

  .footer { position: absolute; left: 0; bottom: 0; width: 100%; height: 25px; border-top: 2px solid var(--rule-dark); background: var(--gold-band); }
  .footer__num {
    position: absolute; left: 17px; top: 7px; width: 9px; height: 9px; border: 1px solid #fff; border-radius: 50%;
    color: #fff; font-size: 5.5px; text-align: center; line-height: 7px;
  }
  .footer__web { position: absolute; left: 0; width: 100%; top: 7px; text-align: center; color: #fff; font-size: 5.5px; letter-spacing: 2.5px; }
  .footer__brand { position: absolute; right: 16px; top: 6px; display: flex; align-items: center; gap: 3px; }
  .footer__brand i { width: 9px; height: 9px; border-radius: 50%; background: #fff; display: block; }
  .footer__brand b { font-family: "Cinzel", Georgia, serif; font-weight: 400; font-size: 5.5px; color: #fff; }

  .photo-frame { position: absolute; left: 17px; top: 87px; width: 206px; height: 157px; border: 2px solid var(--gold); padding: 3px; background: #fff; }
  .photo-frame .photo { width: 100%; height: 100%; background: linear-gradient(135deg, #6b4a30, #b4582a 55%, #8c3c1c); }

  .steps-panel { position: absolute; left: 172px; top: 64px; width: 362px; height: 205px; border: 1px solid var(--panel-line); background: #fff; }
  .steps-svg { position: absolute; left: 0; top: 0; }
  .step { position: absolute; width: 70px; text-align: center; }
  .step__title { font-family: "Cinzel", Georgia, serif; font-size: 6px; color: var(--gold); }
  .step__text { font-size: 4.5px; line-height: 6px; color: var(--ink); }
  .hub-brand { position: absolute; left: 337px; top: 154px; display: flex; align-items: center; gap: 3px; }
  .hub-brand i { width: 12px; height: 12px; border-radius: 50%; background: var(--gold); display: block; }
  .hub-brand b { font-family: "Cinzel", Georgia, serif; font-weight: 400; font-size: 6.5px; color: var(--charcoal); }

  .collage { position: absolute; }
  .tile { position: absolute; border: 3px solid var(--gold-light); }
  .tile--dark { border-color: #555; }

  .back-brand { left: 0; width: 100%; justify-content: center; top: 76px; }
  .back-brand .brand__name { font-size: 17px; }
  .contact { position: absolute; left: 0; width: 100%; top: 156px; text-align: center; }
  .contact__title { font-family: "Cinzel", Georgia, serif; font-size: 13px; color: var(--gold); letter-spacing: .5px; }
  .contact__rule { width: 92px; height: 1px; background: var(--gold); margin: 4px auto 0; }
  .contact__icons { margin: 10px auto 6px; display: flex; justify-content: center; gap: 4px; }
  .contact__line { font-size: 6.5px; line-height: 13px; color: var(--grey-text); }
</style>
</head>
<body>

<!-- Cover page -->
<section class="slide slide--cover">
  <div class="rule" style="top:16px"></div>
  <div class="brand" style="left:22px; top:108px"><span class="brand__dot"></span><span class="brand__name">Bright Ridge Ore</span></div>
  <h1 class="cover-title">PRESENTATION TITLE</h1>
  <p class="cover-text">Lorem Ipsum is simply dummy text of the printing and typesetting industry. Lorem Ipsum has been the industry's standard dummy text ever since the 1500s. When an unknown printer took a galley of type and scrambled it to make a type specimen book.</p>
  <div class="rule" style="top:294px"></div>
</section>
<div class="slide-label" style="left:29px; top:352px">COVER PAGE</div>

<!-- Content page -->
<section class="slide slide--content">
  <header class="page-head">
    <div class="page-head__title">CONTENT <span>PAGE HEADING</span></div>
    <div class="page-head__sub">Content Page subheading</div>
  </header>
  <div class="rule" style="top:46px"></div>
  <div class="steps-panel"></div>
  <div class="photo-frame"><div class="photo" role="img" aria-label="Photo of geologists examining red rock outcrop"></div></div>
  <svg class="steps-svg" width="551" height="310" viewBox="0 0 551 310">
    <defs>
      <radialGradient id="hubGlow" cx="50%" cy="50%" r="50%">
        <stop offset="0.7" stop-color="#ffffff"/>
        <stop offset="1" stop-color="#e4e4e4"/>
      </radialGradient>
    </defs>
    <circle cx="382" cy="164" r="66" fill="#ececec"/>
    <circle cx="382" cy="164" r="50" fill="url(#hubGlow)" stroke="#f3f3f3"/>
    <g fill="none" stroke="#777" stroke-width="0.8">
      <path d="M307 104 H343 V122 H349"/>
      <path d="M307 161 H330"/>
      <path d="M307 218 H329 V200 H335"/>
      <path d="M458 104 H423 V122 H417"/>
      <path d="M458 161 H435"/>
      <path d="M458 218 H436 V200 H430"/>
    </g>
  </svg>
  <div class="step" style="left:236px; top:99px"><div class="step__title">STEP 01</div><div class="step__text">Lorem Ipsum is simply dummy text of the.</div></div>
  <div class="step" style="left:236px; top:156px"><div class="step__title">STEP 02</div><div class="step__text">Lorem Ipsum is simply dummy text of the.</div></div>
  <div class="step" style="left:236px; top:213px"><div class="step__title">STEP 03</div><div class="step__text">Lorem Ipsum is simply dummy text of the.</div></div>
  <div class="step" style="left:460px; top:99px"><div class="step__title">STEP 04</div><div class="step__text">Lorem Ipsum is simply dummy text of the.</div></div>
  <div class="step" style="left:460px; top:156px"><div class="step__title">STEP 05</div><div class="step__text">Lorem Ipsum is simply dummy text of the.</div></div>
  <div class="step" style="left:460px; top:213px"><div class="step__title">STEP 06</div><div class="step__text">Lorem Ipsum is simply dummy text of the.</div></div>
  <div class="hub-brand"><i></i><b>Bright Ridge Ore</b></div>
  <footer class="footer">
    <span class="footer__num">1</span>
    <span class="footer__web">www.webaddress.com</span>
    <span class="footer__brand"><i></i><b>Bright Ridge Ore</b></span>
  </footer>
</section>
<div class="slide-label" style="left:620px; top:352px">INNER PAGE - 1</div>

<!-- Divider page A -->
<section class="slide slide--divider-a">
  <header class="page-head">
    <div class="page-head__title">DIVIDER <span>PAGE HEADING</span></div>
    <div class="page-head__sub">Divider Page subheading</div>
  </header>
  <div class="rule" style="top:46px"></div>
  <svg class="collage" width="551" height="310" viewBox="0 0 551 310">
    <defs>
      <linearGradient id="gMachinery" x1="0" y1="0" x2="0" y2="1"><stop offset="0" stop-color="#b9c2c8"/><stop offset=".5" stop-color="#5a4a3c"/><stop offset="1" stop-color="#6c7a3c"/></linearGradient>
      <linearGradient id="gStorm" x1="0" y1="0" x2="0" y2="1"><stop offset="0" stop-color="#4a5056"/><stop offset=".6" stop-color="#8a9096"/><stop offset="1" stop-color="#b59a5a"/></linearGradient>
      <linearGradient id="gField" x1="0" y1="0" x2="0" y2="1"><stop offset="0" stop-color="#a8b2bc"/><stop offset=".55" stop-color="#6f7a4c"/><stop offset="1" stop-color="#5d6a38"/></linearGradient>
      <linearGradient id="gSky" x1="0" y1="0" x2="0" y2="1"><stop offset="0" stop-color="#9fb4c8"/><stop offset=".7" stop-color="#d5dde4"/><stop offset="1" stop-color="#5a5a3a"/></linearGradient>
      <linearGradient id="gRust" x1="0" y1="0" x2="1" y2="1"><stop offset="0" stop-color="#7a5a48"/><stop offset="1" stop-color="#4a3a34"/></linearGradient>
    </defs>
    <g stroke="#cdb57a" stroke-width="2.5" stroke-linejoin="round">
      <path d="M135 85 L195 145 L135 205 L75 145 Z" fill="url(#gMachinery)" role="img" aria-label="Photo of old mining machinery"/>
      <path d="M229 124 L289 184 L229 244 L169 184 Z" fill="url(#gStorm)" role="img" aria-label="Photo of storm clouds over grassland"/>
      <path d="M323 85 L383 145 L323 205 L263 145 Z" fill="url(#gField)" role="img" aria-label="Photo of fenced paddock with sign"/>
      <path d="M417 124 L477 184 L417 244 L357 184 Z" fill="url(#gSky)" role="img" aria-label="Photo of light aircraft over trees"/>
    </g>
    <g stroke="#555" stroke-width="2" stroke-linejoin="round">
      <path d="M255 96 L277 118 L255 140 L233 118 Z" fill="url(#gRust)" role="img" aria-label="Photo of rusted equipment"/>
      <path d="M388 96 L410 118 L388 140 L366 118 Z" fill="#8a8a6a" role="img" aria-label="Photo of rock sample"/>
      <path d="M162 188 L184 210 L162 232 L140 210 Z" fill="#9a8e84" role="img" aria-label="Photo of core fragments"/>
      <path d="M350 188 L372 210 L350 232 L328 210 Z" fill="#6a6a70" role="img" aria-label="Photo of mineral specimen"/>
    </g>
  </svg>
  <footer class="footer">
    <span class="footer__num">2</span>
    <span class="footer__web">www.webaddress.com</span>
    <span class="footer__brand"><i></i><b>Bright Ridge Ore</b></span>
  </footer>
</section>
<div class="slide-label" style="left:29px; top:728px">INNER PAGE - 2</div>

<!-- Divider page B -->
<section class="slide slide--divider-b">
  <header class="page-head">
    <div class="page-head__title">DIVIDER <span>PAGE HEADING</span></div>
    <div class="page-head__sub">Divider Page subheading</div>
  </header>
  <div class="rule" style="top:46px"></div>
  <div class="tile" role="img" aria-label="Aerial photo of helicopter over desert" style="left:192px; top:53px; width:104px; height:74px; background:linear-gradient(135deg,#d8b878,#b89858)"></div>
  <div class="tile" role="img" aria-label="Photo of geologist in spinifex country" style="left:324px; top:76px; width:83px; height:58px; background:linear-gradient(180deg,#9cb8d4 0 35%,#a0683e 60%,#7a6a3a)"></div>
  <div class="tile tile--dark" role="img" aria-label="Photo of red hills with vehicle" style="left:118px; top:132px; width:75px; height:52px; background:linear-gradient(160deg,#b08a5a,#8a5a2e)"></div>
  <div class="tile" role="img" aria-label="Aerial photo of cleared drill pad" style="left:217px; top:134px; width:102px; height:73px; background:radial-gradient(circle,#a84a24 20%,#c89858 70%); border-color:#555"></div>
  <div class="tile tile--dark" role="img" aria-label="Photo of red rock cliff under blue sky" style="left:329px; top:140px; width:94px; height:66px; background:linear-gradient(160deg,#6a9cd0 0 35%,#b0582a 55%,#7a3a1c)"></div>
  <div class="tile" role="img" aria-label="Aerial photo of open pit mine" style="left:118px; top:188px; width:95px; height:66px; background:linear-gradient(135deg,#c86a3a,#8a3c1c)"></div>
  <div class="tile tile--dark" role="img" aria-label="Photo of rock hammer on red outcrop" style="left:217px; top:218px; width:88px; height:62px; background:linear-gradient(135deg,#a84a24,#6a2c14)"></div>
  <div class="tile" role="img" aria-label="Photo of green valley plains" style="left:309px; top:210px; width:99px; height:70px; background:linear-gradient(180deg,#a8c0d4 0 20%,#a89a3a 45%,#7a8a2a)"></div>
  <footer class="footer">
    <span class="footer__num">3</span>
    <span class="footer__web">www.webaddress.com</span>
    <span class="footer__brand"><i></i><b>Bright Ridge Ore</b></span>
  </footer>
</section>
<div class="slide-label" style="left:620px; top:728px">INNER PAGE - 3</div>

<!-- Back page -->
<section class="slide slide--back">
  <div class="rule" style="top:13px"></div>
  <div class="brand back-brand"><span class="brand__dot"></span><span class="brand__name">Bright Ridge Ore</span></div>
  <div class="contact">
    <div class="contact__title">CONTACT US</div>
    <div class="contact__rule"></div>
    <div class="contact__icons">
      <svg width="9" height="9" viewBox="0 0 10 10"><circle cx="5" cy="5" r="5" fill="#a8862c"/><path d="M5 2.2a1.8 1.8 0 0 1 1.8 1.8C6.8 5.4 5 7.8 5 7.8S3.2 5.4 3.2 4A1.8 1.8 0 0 1 5 2.2z" fill="#fff"/></svg>
      <svg width="9" height="9" viewBox="0 0 10 10"><circle cx="5" cy="5" r="5" fill="#a8862c"/><path d="M3 2.5l1.2 0 .5 1.4-.7.6a4 4 0 0 0 1.5 1.5l.6-.7 1.4.5 0 1.2c-2.6.2-4.7-1.9-4.5-4.5z" fill="#fff"/></svg>
      <svg width="9" height="9" viewBox="0 0 10 10"><circle cx="5" cy="5" r="5" fill="#a8862c"/><rect x="2.6" y="3.2" width="4.8" height="3.4" fill="#fff"/><path d="M2.6 3.2 5 5.1 7.4 3.2" fill="none" stroke="#a8862c" stroke-width=".6"/></svg>
    </div>
    <div class="contact__line">Lorem Ipsum is simply dummy text</div>
    <div class="contact__line">123.456.7890</div>
    <div class="contact__line">info@emailaddress.com</div>
  </div>
  <footer class="footer">
    <span class="footer__web">www.webaddress.com</span>
  </footer>
</section>
<div class="slide-label" style="left:322px; top:1110px">BACK PAGE</div>

</body>
</html>
```